BLORK Business Card

Quellmont Dwelling Additions and Refits. I need a business card designed for this new high end renovation business. I would like the logo centered on the back side with the ABN (71 903 226 417) on the bottom right hand corner.

I would like the following information placed on the other side along with some customized pattern or design.

Percival Oakden
Director
Phone: 1300 418 957
Fax: (02) 9316 4471
Website: www.blorkbuilding.com.au
Email: p.oakden@blorkbuilding.com.au
PO Box 87,
Wendlecove NSW 2094

(FB Logo) BLORK - Quellmont Dwelling Additions and Refits

The final design should communicate professionalism and trust.

Back side background colour: white
Front side: Undecided

```html
<!DOCTYPE html>
<html lang="en">
<head>
<meta charset="utf-8">
<title>BLORK Business Card</title>
<link rel="stylesheet" href="https://fonts.googleapis.com/css2?family=Cinzel:wght@500;700&family=Open+Sans:wght@400;600&display=swap">
<style>
  :root {
    --navy: #3d5b85;
    --navy-dark: #34507a;
    --ink: #2b2b2d;
    --grey-line: #b9bec6;
    --paper: #ffffff;
    --backdrop: #e9e7e3;
  }
  * { margin: 0; padding: 0; box-sizing: border-box; }
  html, body { width: 1200px; height: 1024px; overflow: hidden; }
  body {
    background: var(--backdrop);
    font-family: "Open Sans", Arial, sans-serif;
    color: var(--ink);
    position: relative;
  }
  .card {
    position: absolute;
    left: 220px;
    width: 760px;
    height: 434px;
    background: var(--paper);
    box-shadow: 0 6px 18px rgba(0,0,0,0.18);
    overflow: hidden;
  }
  .card--front { top: 52px; }
  .card--back { top: 538px; }
  .card svg.decor { position: absolute; inset: 0; width: 100%; height: 100%; }

  .brand { position: absolute; text-align: center; }
  .brand__name {
    font-family: "Cinzel", Georgia, serif;
    font-weight: 700;
    color: var(--ink);
    letter-spacing: 4px;
    display: inline-flex;
    align-items: center;
    gap: 14px;
  }
  .brand__dot { width: 14px; height: 14px; border-radius: 50%; background: var(--navy); }
  .brand__tagline {
    font-family: "Cinzel", Georgia, serif;
    font-weight: 500;
    color: var(--navy);
    display: flex;
    align-items: center;
    gap: 10px;
    white-space: nowrap;
  }
  .brand__tagline::before, .brand__tagline::after {
    content: ""; height: 2px; width: 26px; background: var(--navy);
  }

  .card--front .brand { left: 40px; top: 40px; width: 380px; }
  .card--front .brand__name { font-size: 58px; }
  .card--front .brand__tagline { font-size: 15px; margin-top: 4px; justify-content: center; }

  .name-band {
    position: absolute; left: 0; top: 180px; width: 760px; height: 44px;
    color: #fff; font-size: 20px; letter-spacing: 2px; text-transform: uppercase;
  }
  .name-band__name { position: absolute; left: 40px; top: 8px; font-weight: 600; }
  .name-band__role { position: absolute; left: 520px; top: 9px; font-size: 18px; text-transform: none; letter-spacing: 1.5px; }

  .contacts { position: absolute; left: 40px; top: 250px; list-style: none; font-size: 16px; line-height: 25px; }
  .contacts li { display: flex; align-items: center; gap: 10px; }
  .contacts svg { width: 15px; height: 15px; }

  .address { position: absolute; left: 520px; top: 250px; font-size: 15px; line-height: 23px; }

  .website {
    position: absolute; right: 40px; bottom: 22px;
    color: #fff; font-size: 16px; letter-spacing: 2.5px;
  }

  .card--back .brand { left: 0; top: 110px; width: 760px; }
  .card--back .brand__name { font-size: 76px; }
  .card--back .brand__tagline { font-size: 19px; margin-top: 6px; justify-content: center; }

  .abn {
    position: absolute; right: 40px; bottom: 20px;
    color: #fff; font-size: 17px; letter-spacing: 1.5px;
  }
</style>
</head>
<body>

<section class="card card--front" aria-label="Business card front">
  <svg class="decor" viewBox="0 0 760 434" aria-hidden="true">
    <rect x="0" y="180" width="370" height="44" fill="var(--navy)"/>
    <polygon points="370,180 400,190 400,214 370,224" fill="var(--navy-dark)"/>
    <rect x="400" y="186" width="360" height="32" fill="var(--navy)"/>
    <path d="M0,434 L0,396 Q360,322 760,352 L760,434 Z" fill="var(--navy)"/>
    <path d="M0,384 Q360,308 760,340" fill="none" stroke="var(--grey-line)" stroke-width="6"/>
  </svg>

  <div class="brand">
    <div class="brand__name"><span class="brand__dot"></span>BLORK</div>
    <div class="brand__tagline">Quellmont Dwelling Additions &amp; Refits</div>
  </div>

  <div class="name-band">
    <span class="name-band__name">Percival Oakden</span>
    <span class="name-band__role">Director</span>
  </div>

  <ul class="contacts">
    <li><svg viewBox="0 0 16 16" aria-hidden="true"><rect width="16" height="16" rx="2" fill="var(--ink)"/><rect x="5" y="3" width="6" height="10" rx="1" fill="#fff"/></svg>1300 418 957</li>
    <li><svg viewBox="0 0 16 16" aria-hidden="true"><rect width="16" height="16" rx="2" fill="var(--ink)"/><rect x="3" y="6" width="10" height="6" fill="#fff"/><rect x="5" y="3" width="6" height="3" fill="#fff"/></svg>(02) 9316 4471</li>
    <li><svg viewBox="0 0 16 16" aria-hidden="true"><rect width="16" height="16" rx="2" fill="var(--ink)"/><rect x="3" y="4" width="10" height="8" fill="#fff"/><path d="M3,4 L8,9 L13,4" fill="none" stroke="var(--ink)" stroke-width="1.2"/></svg>p.oakden@blorkbuilding.com.au</li>
  </ul>

  <address class="address" style="font-style:normal">PO Box 87,<br>Wendlecove NSW 2094</address>

  <div class="website">www.blorkbuilding.com.au</div>
</section>

<section class="card card--back" aria-label="Business card back">
  <svg class="decor" viewBox="0 0 760 434" aria-hidden="true">
    <path d="M0,434 L0,352 Q380,406 760,352 L760,434 Z" fill="var(--navy)"/>
    <path d="M0,340 Q380,396 760,340" fill="none" stroke="var(--grey-line)" stroke-width="6"/>
  </svg>

  <div class="brand">
    <div class="brand__name"><span class="brand__dot"></span>BLORK</div>
    <div class="brand__tagline">Quellmont Dwelling Additions &amp; Refits</div>
  </div>

  <div class="abn">ABN: 71 903 226 417</div>
</section>

</body>
</html>
```